BRIGHTWAVE PARTNERS NAMECARD

Need to design a name card with an existing logo.

As we are professional corporate services provider our name card has to project a professional image.
Should be corporate, simple & professional.

Our corporate color is maroon red but not too dull.

Please refer to our website at www.brightwavepartners.com.sg

Would attach our logo herewith.

Front surface of namecard details:
BRIGHTWAVE PARTNERS PTE LTD
Registration No. 208731945K

Lowe Hui Ting CA (Singapore)
Director

Tel +65 6481 2957
Mobile +65 9172 3806
lowe@brightwavepartners.com.sg
www.brightwavepartners.com.sg

47 Palmer Lane
#07-14 Harbourlight Plaza
Singapore 274153

Back of namecard:-
OUR CORE SERVICES
Incorporation services
Corporate Secretarial Services
Accountancy service
Goods & Services Taxation
Corporate & Personal Taxation
Financial Reporting
Payroll Administration

AFFILIATES:
TRIVANTA CORPORATE SERVICES PTE LTD
BRIGHTWAVEREGISTRYPTE LTD
ORR MANAGEMENT SERVICES PTE LTD
DW LIM AND COMPANY PTE LTD
LEDGERWISE ACADEMY

```html
<!DOCTYPE html>
<html lang="en">
<head>
<meta charset="utf-8">
<title>Brightwave Partners Namecard</title>
<link rel="stylesheet" href="https://fonts.googleapis.com/css2?family=EB+Garamond:wght@400;600&display=swap">
<style>
  :root {
    --brand-red: #c8192c;
    --card-white: #fbfbfa;
    --backdrop: #8a9394;
    --ink-red: #c01a2c;
  }
  * { box-sizing: border-box; margin: 0; padding: 0; }
  html, body { width: 1200px; height: 1200px; overflow: hidden; }
  body {
    background: var(--backdrop);
    font-family: "EB Garamond", "Times New Roman", serif;
    display: flex;
    flex-direction: column;
    align-items: center;
    justify-content: center;
    gap: 40px;
  }
  .card {
    width: 860px;
    height: 516px;
    background: var(--card-white);
    position: relative;
    overflow: hidden;
    box-shadow: 0 10px 28px rgba(0,0,0,0.22);
  }

  /* Front */
  .card-front .red-field {
    position: absolute;
    left: 0; right: 0;
    top: 74px; bottom: 74px;
    background: var(--brand-red);
    display: flex;
    align-items: center;
    justify-content: center;
  }
  .brand-name-large {
    color: var(--card-white);
    font-weight: 400;
    font-size: 72px;
    line-height: 1;
    white-space: nowrap;
  }

  /* Back */
  .card-back { color: var(--ink-red); }
  .card-back .bottom-band {
    position: absolute;
    left: 0; right: 0; bottom: 0;
    height: 24px;
    background: var(--brand-red);
  }
  .identity {
    position: absolute;
    left: 46px; top: 44px;
    width: 390px;
  }
  .brand-name-small {
    font-weight: 400;
    font-size: 28px;
    line-height: 1;
    white-space: nowrap;
  }
  .registration {
    margin-top: 6px;
    font-size: 11px;
    line-height: 1.3;
    letter-spacing: 0.3px;
  }
  .person-name {
    margin-top: 34px;
    font-weight: 400;
    font-size: 34px;
    line-height: 1.1;
  }
  .person-role {
    font-size: 24px;
    line-height: 1.2;
  }
  .contact-list {
    list-style: none;
    margin-top: 22px;
    font-size: 19px;
    line-height: 1.22;
  }
  .contact-list li {
    display: flex;
    align-items: flex-start;
    gap: 10px;
  }
  .contact-list svg {
    flex: none;
    width: 15px; height: 15px;
    margin-top: 4px;
    fill: var(--ink-red);
  }
  .offer {
    position: absolute;
    left: 452px; top: 48px;
    width: 380px;
  }
  .section-title {
    font-weight: 600;
    font-size: 21px;
    letter-spacing: 0.4px;
    line-height: 1.2;
  }
  .offer-list {
    list-style: none;
    font-size: 16.5px;
    line-height: 1.28;
  }
  .affiliates { margin-top: 26px; }
  .affiliates .offer-list { font-size: 15px; letter-spacing: 0.2px; }
</style>
</head>
<body>

  <section class="card card-front" aria-label="Namecard front">
    <div class="red-field">
      <div class="brand-name-large">Brightwave Partners</div>
    </div>
  </section>

  <section class="card card-back" aria-label="Namecard back">
    <div class="identity">
      <div class="brand-name-small">Brightwave Partners</div>
      <p class="registration">BRIGHTWAVE PARTNERS PTE LTD<br>Registration No. 208731945K</p>
      <h1 class="person-name">Lowe Hui Ting CA</h1>
      <p class="person-role">Director</p>
      <ul class="contact-list">
        <li>
          <svg viewBox="0 0 16 16" aria-hidden="true"><path d="M8 0a5.5 5.5 0 0 0-5.5 5.5C2.5 10 8 16 8 16s5.5-6 5.5-10.5A5.5 5.5 0 0 0 8 0zm0 8a2.5 2.5 0 1 1 0-5 2.5 2.5 0 0 1 0 5z"/></svg>
          <span>47 Palmer Lane<br>#07-14 Harbourlight Plaza<br>Singapore 274153</span>
        </li>
        <li>
          <svg viewBox="0 0 16 16" aria-hidden="true"><path d="M3.6 1l2.2 3.2-1.4 1.6a9 9 0 0 0 5.8 5.8l1.6-1.4L15 12.4 13.3 15C6.6 14.6 1.4 9.4 1 2.7z"/></svg>
          <span>+65 6481 2957</span>
        </li>
        <li>
          <svg viewBox="0 0 16 16" aria-hidden="true"><path d="M4 0h8a1 1 0 0 1 1 1v14a1 1 0 0 1-1 1H4a1 1 0 0 1-1-1V1a1 1 0 0 1 1-1zm1 2v10h6V2zm3 11a1 1 0 1 0 0 2 1 1 0 0 0 0-2z"/></svg>
          <span>+65 9172 3806</span>
        </li>
        <li>
          <svg viewBox="0 0 16 16" aria-hidden="true"><path d="M0 3h16v10H0zm1.5 1.5v.4L8 9l6.5-4.1v-.4zm0 2.2v4.8h13V6.7L8 10.8z"/></svg>
          <span>lowe@brightwavepartners.com.sg</span>
        </li>
        <li>
          <svg viewBox="0 0 16 16" aria-hidden="true"><path d="M8 0a8 8 0 1 0 0 16A8 8 0 0 0 8 0zm5.9 7.2h-2.7a12 12 0 0 0-1-5 6.5 6.5 0 0 1 3.7 5zM8 1.6c.8 1 1.5 3 1.6 5.6H6.4C6.5 4.6 7.2 2.6 8 1.6zM5.8 2.2a12 12 0 0 0-1 5H2.1a6.5 6.5 0 0 1 3.7-5zM2.1 8.8h2.7a12 12 0 0 0 1 5 6.5 6.5 0 0 1-3.7-5zM8 14.4c-.8-1-1.5-3-1.6-5.6h3.2c-.1 2.6-.8 4.6-1.6 5.6zm2.2-.6a12 12 0 0 0 1-5h2.7a6.5 6.5 0 0 1-3.7 5z"/></svg>
          <span>www.brightwavepartners.com.sg</span>
        </li>
      </ul>
    </div>

    <div class="offer">
      <div class="services">
        <h2 class="section-title">OUR CORE SERVICES</h2>
        <ul class="offer-list">
          <li>Incorporation services</li>
          <li>Corporate Secretarial Services</li>
          <li>Accountancy service</li>
          <li>Goods &amp; Services Taxation</li>
          <li>Corporate &amp; Personal Taxation</li>
          <li>Financial Reporting</li>
          <li>Payroll Administration</li>
        </ul>
      </div>
      <div class="affiliates">
        <h2 class="section-title">AFFILIATES:</h2>
        <ul class="offer-list">
          <li>TRIVANTA CORPORATE SERVICES PTE LTD</li>
          <li>BRIGHTWAVEREGISTRYPTE LTD</li>
          <li>ORR MANAGEMENT SERVICES PTE LTD</li>
          <li>DW LIM AND COMPANY PTE LTD</li>
          <li>LEDGERWISE ACADEMY</li>
        </ul>
      </div>
    </div>

    <div class="bottom-band"></div>
  </section>

</body>
</html>
```